Technical Proposal

I have a word document that I would like to make look neat, it will be used for a presentation

Target Market(s)

Information Security or Cyber Security

Industry/Entity Type

Information Technology

Requirements
Must have
• Nice formating and theme to match
Nice to have
• Must look elegant as it will be used as a presentation
Should not have
• Please keep the theme consistent and engaging, should not have random colours

```html
<!DOCTYPE html>
<html lang="en">
<head>
<meta charset="utf-8">
<title>Technical Proposal – Chapter 3</title>
<link href="https://fonts.googleapis.com/css2?family=Montserrat:wght@400;500;600;700;800&display=swap" rel="stylesheet">
<style>
  :root {
    --navy-deep: #17346f;
    --navy: #1f4590;
    --blue-mid: #2c5fb0;
    --blue-light: #4a84cf;
    --accent-blue: #2f7bd0;
    --title-navy: #1c2f55;
    --text-grey: #4b4f57;
    --paper: #ffffff;
  }
  * { margin: 0; padding: 0; box-sizing: border-box; }
  html, body { width: 847px; height: 1200px; overflow: hidden; background: var(--paper); }
  body { font-family: "Montserrat", Arial, sans-serif; }

  .cover {
    position: relative;
    width: 847px;
    height: 1200px;
    background: var(--paper);
  }

  .side-band {
    position: absolute;
    left: 0; top: 0;
    width: 312px;
    height: 1200px;
    background: linear-gradient(180deg, var(--blue-mid) 0%, var(--navy) 45%, var(--navy-deep) 100%);
  }

  .side-band__visual {
    position: absolute;
    left: 0; top: 0;
    width: 312px;
    height: 560px;
    background:
      radial-gradient(ellipse at 40% 38%, rgba(120,170,230,0.45) 0%, rgba(80,130,200,0.15) 45%, rgba(31,69,144,0) 75%),
      linear-gradient(180deg, rgba(74,132,207,0.35) 0%, rgba(31,69,144,0) 100%);
  }

  .cover-titles {
    position: absolute;
    right: 52px;
    top: 442px;
    text-align: right;
    line-height: 34px;
    font-size: 21px;
  }
  .cover-titles__chapter {
    font-weight: 700;
    color: var(--title-navy);
  }
  .cover-titles__doc-type {
    font-weight: 500;
    color: var(--text-grey);
  }
  .cover-titles__topic {
    font-weight: 500;
    color: var(--accent-blue);
  }

  .cover-date {
    position: absolute;
    right: 52px;
    top: 780px;
    font-size: 21px;
    font-weight: 500;
    color: var(--text-grey);
  }

  .brand {
    position: absolute;
    right: 52px;
    top: 1000px;
    display: flex;
    align-items: center;
    gap: 14px;
  }
  .brand__mark {
    width: 34px;
    height: 34px;
    background: var(--navy);
  }
  .brand__name {
    font-size: 24px;
    font-weight: 800;
    color: var(--navy);
    letter-spacing: 0.5px;
  }
</style>
</head>
<body>
  <main class="cover">
    <aside class="side-band">
      <div class="side-band__visual" role="img" aria-label="Blue digital security backdrop with a padlock over circuit lines"></div>
    </aside>

    <section class="cover-titles">
      <p class="cover-titles__chapter">Chapter 3</p>
      <p class="cover-titles__doc-type">Technical Proposal</p>
      <p class="cover-titles__topic">Security Operations Center (SOC)</p>
      <p class="cover-titles__topic">Advanced Cyber Security Controls</p>
      <p class="cover-titles__topic">For Emerging Technologies</p>
      <p class="cover-titles__topic">Cyber Security Awareness</p>
      <p class="cover-titles__topic">Data Loss Prevention (DLP)</p>
    </section>

    <p class="cover-date">Date: 19March 2019</p>

    <div class="brand">
      <span class="brand__mark"></span>
      <span class="brand__name">Harbor Crest Solutions</span>
    </div>
  </main>
</body>
</html>
```